Pull Up Banner - Recruitment Company

We would like a design for a pull up banner.

For context: we are a recruitment business. We specialise in helping people in healthcare industry to find jobs in Australia.

I have come up with several ideas and text for the banner. Feel free to use the following as you see appropriate:

- Our logo (see attached)
- 'Healthcare Recruitment Agency'
- Some sort of imagine / cartoon of medical professionals (ie. doctor, nurse, physiotherapist, speech pathologist). A cartoon is more friendly than committing to a photo
- 'Empowering your next career move'
- 'Discover tailored opportunities based on your career preferences'
- Dot points (allied health, nursing, medical imaging)
- Contact info at the bottom including our website (www.pellatalent.com.au, our Instagram handle @pellatalent, Mobile: XXXX XXX XXX. The title section for contact information could be 'Get in touch:'

Feel free to submit a couple of designs and we can merge aspects that look good on your designs and find the perfect fit.
Thank you
Updates

Hello,

Thank you for your initial submissions to this project. I appreciate the time you've invested.

After reviewing the first attempt, I'd like to share some feedback and initial observations:

- Professionalism and engagement: Is the overall appearance of the banner professional? It's crucial that we have a high-quality design as this will represent our business.

- Image selection: The image (whether cartoon or real people) appears quite generic. Please consider submitting the banner with a few different photos in the middle for us to choose from. Ensure the image is a good fit and not simply a generic stock photo.

- Contact section: Kindly remove the phone number; we no longer wish to include it on the banner. Instead, please include our website (www.pellatalent.com.au) and Instagram handle (@pellatalent).

- Color scheme: White, black, and red/pink are preferred, or alternatively, blue. However, please avoid incorporating too many different colors as it may detract from the professional appearance.

We will be printing the design on a banner and require it to look professional and engaging.

Thank you once again for your submissions. I hope the feedback provided above is helpful.

Warm regards,

Target Market(s)

Allied Health Australia

Font styles to use
Serif

Colors
0054AA
0677BA
7BADD7
CADEEF
E8F1F8
0094D4
00A9DD
6FCCEA
C7EBF8
E9F6FB
EB3D1F
EC4F4E
F09395
F8D3D4
FCEDEE

```html
<!DOCTYPE html>
<html lang="en">
<head>
<meta charset="utf-8">
<title>Pella Talent – Pull Up Banner</title>
<link rel="stylesheet" href="https://fonts.googleapis.com/css2?family=Montserrat:wght@500;700;800;900&family=Open+Sans:wght@500;600&display=swap">
<style>
  :root {
    --brand-blue: #1f2dc6;
    --ink: #0d0d0d;
    --paper: #ffffff;
    --backdrop: #e4e3e4;
    --photo-warm: #c9a77c;
    --photo-teal: #1d9a8e;
    --photo-light: #f1ece6;
  }
  * { margin: 0; padding: 0; box-sizing: border-box; }
  html, body {
    width: 1074px; height: 1200px; overflow: hidden;
    background: var(--backdrop);
  }
  .stage { position: relative; width: 1074px; height: 1200px; }
  .banner {
    position: absolute; left: 306px; top: 40px;
    width: 623px; height: 1510px;
    transform: scale(0.742); transform-origin: top left;
    background: var(--paper);
    overflow: hidden;
    font-family: "Montserrat", sans-serif;
    text-align: center;
    color: var(--ink);
    box-shadow: 0 6px 24px rgba(0,0,0,0.12);
  }
  .brand-name {
    position: absolute; top: 86px; left: 0; width: 100%;
    font-weight: 800; font-size: 56px; letter-spacing: 4px;
    color: var(--ink);
  }
  .headline { position: absolute; top: 222px; left: 0; width: 100%; }
  .headline-main {
    display: block; font-weight: 900; font-size: 74px; line-height: 1;
    color: var(--brand-blue); letter-spacing: 0.5px;
  }
  .headline-sub {
    display: block; margin-top: 4px; font-weight: 800; font-size: 38px;
    line-height: 1; letter-spacing: 1px; color: var(--ink);
  }
  .hero { position: absolute; top: 330px; left: 0; width: 623px; height: 540px; }
  .tagline {
    position: absolute; top: 840px; left: 0; width: 100%;
    font-weight: 900; font-size: 60px; line-height: 58px;
    color: var(--brand-blue);
  }
  .intro {
    position: absolute; top: 1034px; left: 0; width: 100%;
    font-family: "Open Sans", sans-serif; font-weight: 600;
    font-size: 27px; line-height: 34px; color: var(--ink);
  }
  .specialties {
    position: absolute; top: 1158px; left: 0; width: 100%;
    list-style: none; font-weight: 500; font-size: 31px; line-height: 38px;
  }
  .specialties li { display: inline-block; margin: 0 10px; }
  .specialties li::before {
    content: ""; display: inline-block; width: 0; height: 0;
    border-top: 6px solid transparent; border-bottom: 6px solid transparent;
    border-left: 10px solid var(--brand-blue);
    margin-right: 20px; vertical-align: 5px;
  }
  .contact {
    position: absolute; top: 1280px; left: 0; width: 100%; height: 230px;
    background: var(--brand-blue); color: var(--paper);
  }
  .contact-label {
    position: absolute; top: -20px; left: 168px; width: 288px; height: 42px;
    background: var(--ink); border-radius: 16px;
    font-weight: 800; font-size: 28px; line-height: 42px; letter-spacing: 1px;
  }
  .contact-web {
    position: absolute; top: 62px; left: 0; width: 100%;
    font-weight: 500; font-size: 38px; letter-spacing: 0.5px;
  }
  .contact-web strong { font-weight: 800; }
  .contact-social {
    position: absolute; top: 138px; left: 0; width: 100%;
    font-weight: 800; font-size: 30px; letter-spacing: 0.5px;
  }
</style>
</head>
<body>
<div class="stage">
  <article class="banner">
    <div class="brand-name">PELLA TALENT</div>

    <h1 class="headline">
      <span class="headline-main">HEALTHCARE</span>
      <span class="headline-sub">RECRUITMENT AGENCY</span>
    </h1>

    <svg class="hero" viewBox="0 0 623 540" role="img" aria-label="Photo of a smiling nurse in teal scrubs with a stethoscope caring for an elderly woman in a beige cardigan">
      <defs>
        <linearGradient id="hero-tones" x1="0" y1="0" x2="1" y2="0">
          <stop offset="0" stop-color="var(--photo-warm)"/>
          <stop offset="0.45" stop-color="#d8c2a2"/>
          <stop offset="0.6" stop-color="var(--photo-light)"/>
          <stop offset="0.8" stop-color="var(--photo-teal)"/>
          <stop offset="1" stop-color="#e9ecea"/>
        </linearGradient>
      </defs>
      <path d="M0,10 C90,80 190,100 280,96 C400,92 520,40 623,8 L623,512 C580,460 500,424 380,416 C290,410 150,430 0,498 Z" fill="url(#hero-tones)"/>
      <path d="M0,10 C90,80 190,100 280,96 C400,92 520,40 623,8" fill="none" stroke="var(--brand-blue)" stroke-width="6"/>
      <path d="M0,498 C150,430 290,410 380,416 C500,424 580,460 623,512 L623,540 L0,540 Z" fill="var(--paper)"/>
      <path d="M0,498 C150,430 290,410 380,416 C500,424 580,460 623,512" fill="none" stroke="var(--brand-blue)" stroke-width="16"/>
    </svg>

    <h2 class="tagline">EMPOWERING<br>YOUR NEXT<br>CAREER MOVE</h2>

    <p class="intro">Discover tailored opportunities based<br>on your career preferences</p>

    <ul class="specialties">
      <li>ALLIED HEALTH</li><br>
      <li>NURSING</li><li>MEDICAL IMAGING</li>
    </ul>

    <footer class="contact">
      <div class="contact-label">GET IN TOUCH</div>
      <div class="contact-web">www.<strong>pellatalent</strong>.com.au</div>
      <div class="contact-social">@PELLATALENT</div>
    </footer>
  </article>
</div>
</body>
</html>
```